Need a cover for eBook:
Title is: 41 Blunders That Sink Your Indie-Released Volume.
Remarks about the title: I know that is difficult to design a cover with a number. You can add the word TOP (in caps or not) before 41 blunders. It is not mandatory to insert the word TOP. It is up to you if you think you can create a better cover.
Subtitle is: A Newcomer's Manual for Releasing Solo, Arranging Pictures and Words, Planning Pages, Boosting Sign-ups and Moving More Copies
Author: Dennis R. Walbrey
Publisher: Quillmark Press
The book made the presentation of errors that can occur during the production of an ebook. Title must be big, the title should be readable even when the image is reduced in size. No photo please.
I join my projects as an example. Do what you want but I need impact.

Target Market(s)

Book to sell first at Brimfold Reader Shop. Target is authors, men or women, who want to produce ebooks.

Industry/Entity Type

Publishing Company

Font styles to use
Sans Serif

Colors
3176b5
9bcb3c

Requirements
Must have
• High readability when cover is small.
• Here is the definition of the word KILL
• put an end to or cause the failure or defeat of (something).
• "the committee voted to kill the project"
• synonyms: destroy, put an end to, end, extinguish, dash, quash, ruin, wreck, shatter, smash, crush, scotch, thwart; informalput the kibosh on, stymie, scuttle
• "this would kill all hopes of progress"
• veto, defeat, vote down, rule against, reject, throw out, overrule, overturn, put a stop to, quash, squash
• "an opposition attempt to kill the bill"
Nice to have
• I suggested 2 colors but you can you use another one or two. I want cover that sell. There is so bright ideas here. Come on down!
Should not have
• No picture or photo. If a photo or an object had power to the cover, you can insert one. I don't want a photo-collage.

```html
<!DOCTYPE html>
<html lang="en">
<head>
<meta charset="utf-8">
<title>41 Blunders That Sink Your Indie-Released Volume</title>
<link rel="stylesheet" href="https://fonts.googleapis.com/css2?family=Oswald:wght@700&family=Roboto+Condensed:wght@600;700&family=Playfair+Display:wght@400&display=swap">
<style>
  :root {
    --cover-blue: #3176b5;
    --lime: #9bcb3c;
    --title-green: #22a548;
    --ink-blue: #0f4c97;
    --paper: #ffffff;
  }
  html, body {
    margin: 0;
    padding: 0;
    overflow: hidden;
    background: var(--cover-blue);
  }
  .cover {
    position: relative;
    width: 800px;
    height: 1200px;
    overflow: hidden;
    background: var(--cover-blue);
  }
  .cover-art {
    position: absolute;
    inset: 0;
  }
  .big-number {
    font-family: "Playfair Display", serif;
    font-size: 640px;
    fill: var(--lime);
    stroke: var(--cover-blue);
    stroke-width: 7;
    paint-order: stroke;
  }
  .title-line {
    position: absolute;
    left: 60px;
    margin: 0;
    font-family: "Oswald", sans-serif;
    font-weight: 700;
    text-transform: uppercase;
    line-height: 1;
    color: var(--cover-blue);
  }
  .title-line--lead {
    top: 518px;
    font-size: 92px;
    letter-spacing: 1px;
  }
  .title-line--verb {
    top: 612px;
    font-size: 72px;
    letter-spacing: 1px;
  }
  .title-line--object {
    top: 720px;
    left: 0;
    width: 800px;
    text-align: center;
    font-size: 56px;
    color: var(--title-green);
  }
  .subtitle {
    position: absolute;
    top: 830px;
    left: 0;
    width: 800px;
    text-align: center;
    font-family: "Roboto Condensed", sans-serif;
    color: var(--ink-blue);
  }
  .subtitle-lead {
    margin: 0 0 6px;
    font-family: "Oswald", sans-serif;
    font-weight: 700;
    font-size: 29px;
    letter-spacing: 2px;
    text-transform: uppercase;
  }
  .subtitle-body {
    margin: 0;
    font-weight: 600;
    font-size: 28px;
    line-height: 35px;
  }
  .subtitle-accent {
    color: var(--title-green);
  }
  .author {
    position: absolute;
    top: 1072px;
    left: 0;
    width: 800px;
    margin: 0;
    text-align: center;
    font-family: "Roboto Condensed", sans-serif;
    font-weight: 700;
    font-size: 32px;
    letter-spacing: 4px;
    text-transform: uppercase;
    color: var(--paper);
  }
  .publisher {
    position: absolute;
    top: 1126px;
    left: 0;
    width: 800px;
    margin: 0;
    text-align: center;
    font-family: "Roboto Condensed", sans-serif;
    font-weight: 700;
    font-size: 19px;
    color: var(--paper);
  }
</style>
</head>
<body>
  <main class="cover">
    <svg class="cover-art" width="800" height="1200" viewBox="0 0 800 1200" aria-hidden="true">
      <ellipse class="spotlight" cx="400" cy="515" rx="440" ry="530" fill="var(--paper)"/>
      <text class="big-number" x="405" y="515" text-anchor="middle">41</text>
    </svg>

    <h1 class="title">
      <span class="title-line title-line--lead">Blunders</span>
      <span class="title-line title-line--verb">That Sink</span>
      <span class="title-line title-line--object">Your Indie-Released Volume</span>
    </h1>

    <div class="subtitle">
      <p class="subtitle-lead">A Newcomer's Manual for</p>
      <p class="subtitle-body">
        Releasing Solo, Arranging Pictures and Words,<br>
        Planning Pages, Boosting Sign-ups<br>
        and <span class="subtitle-accent">Moving More Copies</span>
      </p>
    </div>

    <p class="author">Dennis R. Walbrey</p>
    <p class="publisher">Published by Quillmark Press</p>
  </main>
</body>
</html>
```